Flyer for corporate discount for dog daycare

I own a dog daycare with a large corporate down the road. I am working with the President of the company to offer their employees a discount for my services, Dog Daycare, Overnight Care, Grooming Salon & Spa and Retail. The design should be professional but also have a soft side as people view their dogs similar to human children.

I attached my logo along with our grooming brochure for reference on colors we've been using.

At a minimum the flyer must contain the following information:
Name: The Wagtail Lodge
web address: www.PawHavenStays.example
phone number: 920-555-0148
Address: 4872 Larchmont Lane
Google Map of our location

Title of flyer/program: Corporate V.I.P. (Very Important Pooch) (Can be creative with how to include this such as, Welcome to our Corporate. . .. etc.)

The program offer is: 5% discount
My services: Dog Daycare, Overnight Care, Grooming Salon & Spa and Retail

Target Market(s)

corporate employees, male and female, age 24+

Industry/Entity Type

Daycare

Requirements
Must have
• Must be easy to read and inviting.
Nice to have
• Nice photo dogs playing or inviting photo of dog.
Should not have
• cartoon feel

```html
<!DOCTYPE html>
<html lang="en">
<head>
<meta charset="utf-8">
<title>The Wagtail Lodge – Corporate V.I.P. Flyer</title>
<link href="https://fonts.googleapis.com/css2?family=Montserrat:wght@500;600;700&display=swap" rel="stylesheet">
<style>
  :root {
    --leaf: #8cc63f;
    --leaf-deep: #76b12e;
    --leaf-soft: rgba(196, 226, 150, 0.82);
    --sky: #acdfe6;
    --white: #ffffff;
    --bark: #5b4a3f;
    --gold: #f0c96a;
    --photo-light: #d9e4c6;
    --photo-mid: #a9b98e;
    --photo-dark: #8f8c7e;
    --map-tone: #ece8df;
  }
  * { margin: 0; padding: 0; box-sizing: border-box; }
  html, body {
    width: 927px; height: 1200px; overflow: hidden; background: var(--white);
  }
  .flyer {
    position: relative; width: 927px; height: 1200px; overflow: hidden;
    font-family: "Montserrat", Arial, sans-serif; color: var(--white);
  }
  .hero-photo {
    position: absolute; left: 0; top: 0; width: 927px; height: 580px;
    background:
      radial-gradient(ellipse 260px 230px at 420px 250px, #f4f3ef 0%, #e9e7e0 55%, rgba(233,231,224,0) 100%),
      linear-gradient(180deg, var(--photo-light) 0%, var(--photo-mid) 45%, var(--photo-dark) 100%);
  }
  .backdrop { position: absolute; left: 0; top: 0; }
  .brand-disc {
    position: absolute; left: 560px; top: -110px; width: 470px; height: 470px;
    border-radius: 50%; background: var(--leaf-soft);
  }
  .brand {
    position: absolute; left: 690px; top: 60px; width: 180px; text-align: center;
  }
  .brand-mark {
    display: block; width: 76px; height: 76px; margin: 0 auto 14px;
    background: var(--bark);
  }
  .brand-name {
    font-size: 22px; font-weight: 600; color: var(--bark); letter-spacing: 1px; line-height: 1.2;
  }
  .brand-rule {
    display: block; width: 110px; height: 2px; margin: 18px auto 0; background: var(--white);
  }
  .offer {
    position: absolute; left: 68px; top: 650px; width: 794px; text-align: center;
  }
  .offer-title {
    font-size: 26px; font-weight: 700; letter-spacing: 4px; line-height: 32px;
  }
  .offer-title .accent { color: var(--leaf); }
  .offer-line {
    margin-top: 22px; font-size: 16px; font-weight: 700;
  }
  .offer-line .deal { color: var(--leaf-deep); font-size: 24px; }
  .services-title {
    margin-top: 22px; font-size: 22px; font-weight: 600; letter-spacing: 4px;
  }
  .services {
    position: absolute; left: 456px; top: 830px; list-style: none;
    font-size: 19px; font-weight: 600; letter-spacing: 2.5px; line-height: 37px;
  }
  .services li { display: flex; align-items: center; gap: 12px; }
  .services li::before { content: "•"; }
  .services .tick { width: 24px; height: 20px; }
  .services .cont { padding-left: 42px; margin-top: -10px; }
  .services .cont::before { content: ""; }
  .location-map {
    position: absolute; left: 27px; top: 927px; width: 276px; height: 251px;
    background: linear-gradient(135deg, var(--map-tone) 0%, #ddd8cc 100%);
  }
  .contact {
    position: absolute; display: flex; align-items: center; gap: 10px;
    font-size: 17px; font-weight: 600; white-space: nowrap;
  }
  .contact svg { flex: none; }
  .contact-address { left: 515px; top: 1104px; }
  .contact-phone { left: 372px; top: 1150px; }
  .contact-web { left: 548px; top: 1150px; }
</style>
</head>
<body>
<main class="flyer">
  <div class="hero-photo" role="img" aria-label="Photo of a white puppy with a green collar lying on a sunlit wooden deck"></div>

  <div class="brand-disc"></div>
  <div class="brand">
    <span class="brand-mark"></span>
    <p class="brand-name">The Wagtail Lodge</p>
    <span class="brand-rule"></span>
  </div>

  <svg class="backdrop" width="927" height="1200" viewBox="0 0 927 1200" aria-hidden="true">
    <path d="M0 560 Q460 505 927 545 V1200 H0 Z" fill="var(--leaf)"/>
    <path d="M0 580 Q460 525 927 560" fill="none" stroke="var(--white)" stroke-opacity=".5" stroke-width="1.5"/>
    <path d="M0 592 Q470 540 927 572" fill="none" stroke="var(--gold)" stroke-opacity=".6" stroke-width="1.2"/>
    <path d="M68 628 H862 V1030 Q600 1064 345 1068 Q322 1068 322 1045 V935 Q322 898 285 890 Q170 868 68 845 Z"
          fill="var(--sky)"/>
    <path d="M68 845 Q170 868 285 890 Q322 898 322 935 V1045" fill="none" stroke="var(--white)" stroke-width="3"/>
    <path d="M330 1085 Q620 1082 927 1040" fill="none" stroke="var(--white)" stroke-opacity=".6" stroke-width="1.5"/>
    <path d="M330 1095 Q620 1092 927 1055" fill="none" stroke="var(--gold)" stroke-opacity=".6" stroke-width="1.2"/>
  </svg>

  <section class="offer">
    <h1 class="offer-title">Welcome to our Corporate <span class="accent">V.I.P.</span><br>(Very Important Pooch)</h1>
    <p class="offer-line">The program offer is: <span class="deal">-5% discount</span></p>
    <h2 class="services-title">Our services:</h2>
  </section>

  <ul class="services">
    <li>Dog Daycare <svg class="tick" viewBox="0 0 24 20"><path d="M2 11 L9 17 L22 3" fill="none" stroke="var(--leaf-deep)" stroke-width="4" stroke-linecap="round" stroke-linejoin="round"/></svg></li>
    <li>Overnight Care <svg class="tick" viewBox="0 0 24 20"><path d="M2 11 L9 17 L22 3" fill="none" stroke="var(--leaf-deep)" stroke-width="4" stroke-linecap="round" stroke-linejoin="round"/></svg></li>
    <li>Grooming Salon <svg class="tick" viewBox="0 0 24 20"><path d="M2 11 L9 17 L22 3" fill="none" stroke="var(--leaf-deep)" stroke-width="4" stroke-linecap="round" stroke-linejoin="round"/></svg></li>
    <li class="cont">&amp; Spa and Retail</li>
  </ul>

  <div class="location-map" role="img" aria-label="Street map showing the location of The Wagtail Lodge"></div>

  <p class="contact contact-address">
    <svg width="22" height="30" viewBox="0 0 22 30"><path d="M11 1 C5 1 1 5.5 1 11 C1 18 11 29 11 29 C11 29 21 18 21 11 C21 5.5 17 1 11 1 Z" fill="var(--white)"/><circle cx="11" cy="11" r="4" fill="var(--leaf)"/></svg>
    4872 Larchmont Lane
  </p>
  <p class="contact contact-phone">
    <svg width="20" height="32" viewBox="0 0 20 32"><rect x="1" y="1" width="18" height="30" rx="3" fill="var(--white)"/><rect x="4" y="5" width="12" height="16" fill="var(--leaf)"/><circle cx="10" cy="26" r="2" fill="var(--leaf)"/></svg>
    920-555-0148
  </p>
  <p class="contact contact-web">
    <svg width="34" height="34" viewBox="0 0 34 34"><circle cx="16" cy="16" r="14" fill="none" stroke="var(--white)" stroke-width="2.5"/><ellipse cx="16" cy="16" rx="6" ry="14" fill="none" stroke="var(--white)" stroke-width="2"/><path d="M2 16 H30 M5 9 H27 M5 23 H27" stroke="var(--white)" stroke-width="2"/><path d="M20 18 L32 24 L26 26 L24 32 Z" fill="var(--white)" stroke="var(--leaf)" stroke-width="1"/></svg>
    www.PawHavenStays.example
  </p>
</main>
</body>
</html>
```